QMB Vane Works

- Brochure design

Target Market(s)

Granite and Quartz

Font styles to use
Sans Serif

Colors

Designer to choose colors to be used in the design.

Requirements
Must have
• I post the instruction file below
Nice to have
Should not have

```html
<!DOCTYPE html>
<html lang="en">
<head>
<meta charset="utf-8">
<title>QMB Vane Works – Size Chart</title>
<link rel="stylesheet" href="https://fonts.googleapis.com/css2?family=Lato:wght@300;400;700;900&display=swap">
<style>
:root{
  --backdrop:#3c3b3d;
  --paper:#ffffff;
  --paper-shade:#dcdcde;
  --ink:#111111;
  --rule:#232a44;
  --rule-light:#6b7084;
  --label:#555555;
  --stone-dark:#5b5b5e;
  --stone-mid:#a69d90;
  --stone-light:#e6e4e0;
}
*{margin:0;padding:0;box-sizing:border-box}
html,body{width:1200px;height:774px;overflow:hidden;background:var(--backdrop)}
body{position:relative;font-family:"Lato",sans-serif;color:var(--ink)}
.page{position:absolute;top:65px;width:498px;height:644px;background:linear-gradient(90deg,var(--paper) 0%,var(--paper) 62%,var(--paper-shade) 100%);overflow:hidden}
.page--left{left:96px}
.page--right{left:607px}
.page-title{position:absolute;left:39px;top:38px;font-weight:300;font-size:24px;letter-spacing:.5px;color:#2a2a2a}
.rule-thin{position:absolute;left:32px;right:0;top:92px;height:1px;background:var(--rule)}
.rule-thick{position:absolute;left:32px;right:0;top:97px;height:3px;background:var(--rule)}
.section-head{position:absolute;left:50px;top:106px}
.section-head h2{font-weight:900;font-size:17px;line-height:18px;letter-spacing:-.2px}
.section-head p{font-weight:300;font-size:11px;line-height:12px}
.size-table{position:absolute;border-collapse:collapse;font-size:9.5px;font-weight:400}
.size-table td{border:1px solid var(--ink);height:15px;padding:0 4px;white-space:nowrap}
.photo{position:absolute;top:111px;height:152px}
.outline{position:absolute;border:1.5px solid var(--ink);border-radius:4px}
.dim{position:absolute;font-size:5.5px;font-weight:700;white-space:nowrap}
.swatch{position:absolute;width:78px;height:32px;border-radius:2px;transform:skewX(-12deg)}
.profile{position:absolute;width:36px;height:6px;border:1px solid #bbb;border-radius:1px}
.code{position:absolute;font-size:6px;letter-spacing:1px;color:var(--label)}
.drawing{position:absolute;width:120px;height:61px;top:276px;border:1px solid #c8c8c8;background:#f4f4f4}
.product{position:absolute;width:118px;height:54px;border-radius:3px;transform:skewX(-14deg)}
.prod-name{position:absolute;width:140px;font-size:6px;text-align:center;color:var(--label);text-transform:uppercase}
.footer-url{position:absolute;left:19px;top:612px;font-size:9.5px;color:#333}
.footer-rule{position:absolute;left:132px;right:0;top:618px;height:1px;background:var(--rule-light)}
.page--right .footer-rule{left:134px}
</style>
</head>
<body>

<!-- Kitchen countertops page -->
<section class="page page--left">
  <h1 class="page-title">Size Chart</h1>
  <div class="rule-thin"></div><div class="rule-thick"></div>
  <div class="section-head"><h2>Kitchen Countertops</h2><p>American Standard Size</p></div>
  <table class="size-table" style="left:51px;top:141px;width:167px">
    <tr><td>98"x26"x3/4"</td><td>96"x25 1/2"X3CM</td></tr>
    <tr><td>110"x26"x3/4"</td><td>108"x25 1/2" X3CM</td></tr>
    <tr><td>98"x36"x3/4"</td><td>96"x36"X3CM</td></tr>
    <tr><td>110"x36"x3/4"</td><td>108"x36" X3CM</td></tr>
    <tr><td>98"x42"x3/4"</td><td>96"x42"X3CM</td></tr>
    <tr><td>110"x42"x3/4"</td><td>108"x42" X3CM</td></tr>
    <tr><td>98"x52"x3/4"</td><td>96"x52"X3CM</td></tr>
    <tr><td>110"x52"x3/4"</td><td>108"x52" X3CM</td></tr>
  </table>
  <div class="photo" role="img" aria-label="Cream kitchen with dark wood island and light stone countertop" style="left:223px;width:244px;background:linear-gradient(135deg,#e9dcb8 0%,#cdb98e 45%,#5a3a22 75%,#c9b38a 100%)"></div>

  <div class="outline" style="left:50px;top:268px;width:127px;height:13px"></div>
  <div class="dim" style="left:95px;top:290px">98" x 4"&nbsp;&nbsp;&nbsp;100'x4"</div>
  <div class="outline" style="left:50px;top:300px;width:127px;height:30px"></div>
  <div class="dim" style="left:82px;top:338px">98" x 26"&nbsp;&nbsp;&nbsp;110'x26"</div>
  <div class="outline" style="left:193px;top:268px;width:126px;height:62px"></div>
  <div class="dim" style="left:225px;top:338px">98' x 36'&nbsp;&nbsp;&nbsp;110'x36"</div>
  <div class="outline" style="left:340px;top:268px;width:127px;height:62px"></div>
  <div class="dim" style="left:343px;top:335px">98' x 42"&nbsp;&nbsp;98" x 52"&nbsp;&nbsp;110"x42"&nbsp;&nbsp;110"x52"</div>

  <div class="swatch" role="img" aria-label="Dark granite edge sample" style="left:58px;top:351px;background:linear-gradient(#6e6e70,#48484a)"></div>
  <div class="swatch" role="img" aria-label="Speckled granite edge sample" style="left:163px;top:351px;background:linear-gradient(#a7a196,#7e776b)"></div>
  <div class="swatch" role="img" aria-label="Brown granite edge sample" style="left:268px;top:351px;background:linear-gradient(#b5a493,#85766a)"></div>
  <div class="swatch" role="img" aria-label="Grey granite edge sample" style="left:373px;top:351px;background:linear-gradient(#8d8e92,#5f6064)"></div>
  <div class="profile" style="left:56px;top:394px"></div><div class="code" style="left:117px;top:397px">LDE01</div>
  <div class="profile" style="left:161px;top:394px"></div><div class="code" style="left:222px;top:397px">LDE02</div>
  <div class="profile" style="left:266px;top:394px"></div><div class="code" style="left:327px;top:397px">LDE03</div>
  <div class="profile" style="left:371px;top:394px"></div><div class="code" style="left:432px;top:397px">LDE04</div>

  <div class="swatch" role="img" aria-label="Dark granite edge sample" style="left:58px;top:413px;background:linear-gradient(#6a6664,#3f3b39)"></div>
  <div class="swatch" role="img" aria-label="Gold granite edge sample" style="left:163px;top:413px;background:linear-gradient(#e6dfcf,#b8ab8c)"></div>
  <div class="swatch" role="img" aria-label="White granite edge sample" style="left:268px;top:413px;background:linear-gradient(#ececee,#b3b5ba)"></div>
  <div class="swatch" role="img" aria-label="Beige granite edge sample" style="left:373px;top:413px;background:linear-gradient(#d6cab0,#a99a7c)"></div>
  <div class="profile" style="left:56px;top:456px"></div><div class="code" style="left:117px;top:459px">LDE05</div>
  <div class="profile" style="left:161px;top:456px"></div><div class="code" style="left:222px;top:459px">LDE06</div>
  <div class="profile" style="left:266px;top:456px"></div><div class="code" style="left:327px;top:459px">LDE07</div>
  <div class="profile" style="left:371px;top:456px"></div><div class="code" style="left:432px;top:459px">LDE08</div>

  <div class="swatch" role="img" aria-label="Blue grey granite edge sample" style="left:58px;top:485px;background:linear-gradient(#a8adb8,#6f7482)"></div>
  <div class="swatch" role="img" aria-label="Tan granite edge sample" style="left:163px;top:485px;background:linear-gradient(#b4a591,#857562)"></div>
  <div class="swatch" role="img" aria-label="Dark granite edge sample" style="left:268px;top:485px;background:linear-gradient(#7c8088,#4b4e55)"></div>
  <div class="swatch" role="img" aria-label="Brown granite edge sample" style="left:373px;top:485px;background:linear-gradient(#a59581,#6f6253)"></div>
  <div class="profile" style="left:56px;top:528px"></div><div class="code" style="left:117px;top:533px">LDE09</div>
  <div class="profile" style="left:161px;top:528px"></div><div class="code" style="left:222px;top:533px">LDE10</div>
  <div class="profile" style="left:266px;top:528px"></div><div class="code" style="left:327px;top:533px">LDE11</div>
  <div class="profile" style="left:371px;top:528px"></div><div class="code" style="left:432px;top:533px">LDE12</div>

  <div class="swatch" role="img" aria-label="Gold granite edge sample" style="left:58px;top:551px;background:linear-gradient(#d3c6a8,#9f8f6f)"></div>
  <div class="swatch" role="img" aria-label="Light granite edge sample" style="left:163px;top:551px;background:linear-gradient(#d2ccc2,#a29a8d)"></div>
  <div class="swatch" role="img" aria-label="Black granite edge sample" style="left:268px;top:551px;background:linear-gradient(#3a3838,#161515)"></div>
  <div class="profile" style="left:56px;top:594px"></div><div class="code" style="left:117px;top:598px">LDE13</div>
  <div class="profile" style="left:161px;top:594px"></div><div class="code" style="left:222px;top:598px">LDE14</div>
  <div class="profile" style="left:266px;top:594px"></div><div class="code" style="left:327px;top:598px">LDE15</div>

  <div class="footer-url">www.qmbvaneworks.com</div><div class="footer-rule"></div>
</section>

<!-- Vanity tops page -->
<section class="page page--right">
  <h1 class="page-title">Size Chart</h1>
  <div class="rule-thin"></div><div class="rule-thick"></div>
  <div class="section-head" style="left:51px"><h2>Vanity Tops</h2><p>American Standard Size</p></div>
  <table class="size-table" style="left:52px;top:143px;width:145px">
    <tr><td>25"x22"x3/4"</td><td>25"X22"3CM</td></tr>
    <tr><td>31"x22"x3/4"</td><td>31"X22"3CM</td></tr>
    <tr><td>37"x22"x3/4"</td><td>37"X22"3CM</td></tr>
    <tr><td>43"x22"x3/4"</td><td>43"X22"3CM</td></tr>
    <tr><td>49"x22"x3/4"</td><td>49"X22"3CM</td></tr>
    <tr><td>61"x22"x3/4"</td><td>61X22"3CM</td></tr>
    <tr><td>73"x22"x3/4"</td><td>73"X22"3CM</td></tr>
  </table>
  <div class="photo" role="img" aria-label="Kitchen island with grey cabinets and thick concrete-look stone top" style="left:224px;width:243px;background:linear-gradient(135deg,#d6d2cc 0%,#a9a49d 40%,#4d4f54 65%,#b59a80 100%)"></div>

  <div class="drawing" role="img" aria-label="Technical drawing of vanity top with oval sink" style="left:41px"></div>
  <div class="drawing" role="img" aria-label="Technical drawing of vanity top with rectangular sink" style="left:190px"></div>
  <div class="drawing" role="img" aria-label="Technical drawing of banjo vanity top" style="left:338px"></div>
  <div class="prod-name" style="left:31px;top:341px;text-transform:none">Vanity Top</div>
  <div class="prod-name" style="left:180px;top:341px;text-transform:none">Vanity Top</div>
  <div class="prod-name" style="left:328px;top:341px;text-transform:none">Banjo Vanity Top</div>

  <div class="product" role="img" aria-label="White quartz vanity top with sink" style="left:48px;top:361px;background:linear-gradient(#f4f4f4,#d8d8da)"></div>
  <div class="product" role="img" aria-label="Grey quartz vanity top with sink" style="left:196px;top:361px;background:linear-gradient(#e6e6e8,#bdbdc0)"></div>
  <div class="product" role="img" aria-label="White marble vanity top with sink" style="left:345px;top:361px;background:linear-gradient(#ebebea,#c6c6c4)"></div>
  <div class="prod-name" style="left:36px;top:419px">VT-Crystal White Quartz</div>
  <div class="prod-name" style="left:184px;top:419px">VT-Crystal Grey Quartz</div>
  <div class="prod-name" style="left:333px;top:418px">VT-Carrara White</div>

  <div class="product" role="img" aria-label="Cream marble vanity top with faucet" style="left:48px;top:448px;background:linear-gradient(#f1e8cf,#dccca3)"></div>
  <div class="product" role="img" aria-label="Brown granite vanity top with faucet" style="left:196px;top:448px;background:linear-gradient(#7a6656,#4a3a30)"></div>
  <div class="product" role="img" aria-label="Gold granite vanity top with faucet" style="left:345px;top:448px;background:linear-gradient(#dcc7a3,#b59c73)"></div>
  <div class="prod-name" style="left:36px;top:507px">VT-Cremamarfil</div>
  <div class="prod-name" style="left:184px;top:506px">VT-Tan Brown</div>
  <div class="prod-name" style="left:333px;top:506px">VT-New Venetian Gold</div>

  <div class="product" role="img" aria-label="Black granite double vanity top" style="left:48px;top:531px;background:linear-gradient(#3b3a3a,#151414)"></div>
  <div class="product" role="img" aria-label="Golden granite vanity top with oval sink" style="left:196px;top:531px;background:linear-gradient(#ece0bf,#cdb98c)"></div>
  <div class="product" role="img" aria-label="Dark gold granite vanity top with faucet" style="left:345px;top:531px;background:linear-gradient(#dcc196,#b3925f)"></div>
  <div class="prod-name" style="left:36px;top:589px">VT-Mongolian Black</div>
  <div class="prod-name" style="left:184px;top:588px">VT-Golden Garnet</div>
  <div class="prod-name" style="left:333px;top:588px">VT-Santa Cecilia Dark</div>

  <div class="footer-url">www.qmbvaneworks.com</div><div class="footer-rule"></div>
</section>

</body>
</html>
```